Fresh & Clean *NEW* BUSINESS CARD Needed - OPTOMETRY Clinic/Optical

High-tech optometry practice with 3 doctors seeking new business card.  We provide eye exams, sell, designer glasses/contacts/specialty eyewear and treat ocular diseases.  For our business cards, we are seeking fresh, clean, and crisp design as we grow our team (staffing change).  Simply adding doctors is making the card look busy/cluttered.
 Looking for professional, less cluttered look yet still have our logo, doctor names, phone, address, and website....If possible!  :)
Names:
Marcia Trelford, O.D.
Ned Pallister, O.D.
Oona Ferrant, O.D.
Phone: 555-014-2738
Website: www.BrightLensHub.example
Address:  417 Garnet R. Holloway, Harlow Springs, ZQ 00000
Ultimately we have the main business card with all doctor sames and that card has two versions  (front is always the same).  The back has two designs (1) displays next appointment time/date, (2) for "general use" (non-appointment.)    I have attached what we have used in the past.  
We also need a design template for each team member in our practice with their name, title, and email.   Those should be designed with the "general use" back (see attached).
**Open to entirely new design so don't feel obligated to keep current format.  Need new perspective!  Also including our watermark and some other design features we have consistently used in past in our portfolio.  Included are two options for logos--vertical and horizontal.
**I also would like to remove "Member of Sight Alliance" on our logo if possible**
 Other image files available upon request.

Target Market(s)

New patient & Current Patients

Industry/Entity Type

Optometry

Contact Information for Business Card

High-tech optometry practice with 3 doctors seeking new business card.  We provide eye exams, sell, designer glasses/contacts/specialty eyewear and treat ocular diseases.  For our business cards, we are seeking fresh, clean, and crisp design as we grow our team (staffing change).  Simply adding doctors is making the card look busy/cluttered.  Looking for professional, less cluttered look yet still have our logo, doctor names, phone, address, and website....If possible!  :) Names: Marcia Trelford, O.D. Ned Pallister, O.D. Oona Ferrant, O.D. Phone: 555-014-2738 Website: www.BrightLensHub.example Address:  417 Garnet R. Holloway, Harlow Springs, ZQ 00000 Ultimately we have the main business card with all doctor sames and that card has two versions  (front is always the same).  The back has two designs (1) displays next appointment time/date, (2) for "general use" (non-appointment.)    I have attached what we have used in the past.   We also need a design template for each team member in our practice with their name, title, and email.   Those should be designed with the "general use" back (see attached). **Open to entirely new design so don't feel obligated to keep current format.  Need new perspective!  Also including our watermark and some other design features we have consistently used in past in our portfolio.  Included are two options for logos--vertical and horizontal. **I also would like to remove "Member of Sight Alliance" on our logo if possible**  Other image files available upon request.

Font styles to use
Other font styles liked:
• We have used Montserrat / Yellowtail in the past

Colors

Designer to choose colors to be used in the design.

Requirements
Must have
• Clean & Fresh Design with Logo / Info provided in description. Horizontal orientation. **I have included the CMYK colors we currently have in our logo.
Should not have
• Cluttered

```html
<!DOCTYPE html>
<html lang="en">
<head>
<meta charset="utf-8">
<title>BrightLens Hub – Business Card Front and Appointment Back</title>
<link href="https://fonts.googleapis.com/css2?family=Montserrat:wght@300;400;500;600&display=swap" rel="stylesheet">
<style>
  :root {
    --backdrop: #b5b5b5;
    --card-light: #ebebeb;
    --card-white: #ffffff;
    --slate: #31383f;
    --gold: #e3b936;
    --olive: #6b5e2a;
    --ink: #4c5058;
    --ink-soft: #6a6c70;
    --logo-grey: #6d6e70;
    --iris: #a6dbe6;
    --rule: #2d3338;
  }
  * { box-sizing: border-box; margin: 0; padding: 0; }
  html, body { width: 1200px; height: 1200px; overflow: hidden; }
  body {
    background: var(--backdrop);
    font-family: "Montserrat", Arial, sans-serif;
    position: relative;
  }
  .card {
    position: absolute;
    left: 179px;
    width: 862px;
    height: 496px;
    overflow: hidden;
    box-shadow: 0 10px 22px rgba(0,0,0,0.28);
  }
  .card--front { top: 84px; background: var(--card-light); }
  .card--back { top: 621px; background: var(--card-white); }

  .brand {
    position: absolute;
    left: 0; right: 0;
    height: 80px;
    display: flex;
    justify-content: center;
    align-items: center;
    gap: 14px;
  }
  .brand__dot {
    width: 76px; height: 76px;
    border-radius: 50%;
    background: var(--iris);
  }
  .brand__name {
    font-size: 60px;
    font-weight: 400;
    color: var(--logo-grey);
    letter-spacing: 3px;
    line-height: 1;
  }
  .card--front .brand { top: 28px; }
  .card--back .brand { top: 28px; }

  .doctors {
    position: absolute;
    top: 128px; left: 0; right: 0;
    text-align: center;
    color: var(--ink);
    font-size: 40px;
    font-weight: 500;
    line-height: 45px;
  }
  .gold-rule {
    position: absolute;
    top: 278px; left: 0; right: 0;
    height: 8px;
    background: var(--gold);
  }
  .contact {
    position: absolute;
    top: 286px; left: 0; right: 0; bottom: 0;
    background: var(--slate);
    color: #fff;
    text-align: center;
    font-size: 31px;
    font-weight: 500;
  }
  .contact__line {
    display: flex;
    justify-content: center;
    align-items: center;
    gap: 14px;
    height: 42px;
  }
  .contact__line:first-child { margin-top: 14px; }
  .contact__icon { width: 22px; height: 22px; }
  .contact__accent { color: var(--gold); }
  .contact__address { margin-top: 10px; letter-spacing: 0.3px; }

  .appt-band {
    position: absolute;
    top: 142px; left: 0; right: 0;
    height: 62px;
    background: var(--slate);
    color: #fff;
    font-size: 31px;
    font-weight: 500;
    letter-spacing: 0.8px;
    display: flex; align-items: center; justify-content: center;
  }
  .appt-table {
    position: absolute;
    top: 236px; left: 35px;
    width: 776px; height: 152px;
    border: 1.5px solid var(--rule);
    display: flex;
  }
  .appt-table__cell {
    flex: 0 0 auto;
    text-align: center;
    font-size: 32px;
    font-weight: 500;
    color: var(--slate);
    padding-top: 4px;
    letter-spacing: 0.5px;
  }
  .appt-table__cell--date { width: 383px; border-right: 1.5px solid var(--rule); }
  .appt-table__cell--time { flex: 1; }
  .appt-note {
    position: absolute;
    top: 403px; left: 0; right: 0;
    text-align: center;
    font-size: 28px;
    font-weight: 500;
    color: var(--ink-soft);
    line-height: 35px;
  }
  .olive-rule {
    position: absolute;
    bottom: 0; left: 0; right: 0;
    height: 7px;
    background: var(--olive);
  }
</style>
</head>
<body>

<section class="card card--front">
  <div class="brand">
    <span class="brand__dot"></span>
    <span class="brand__name">brightlenshub</span>
  </div>

  <div class="doctors">
    <p>Marcia Trelford, O.D.</p>
    <p>Ned Pallister, O.D.</p>
    <p>Oona Ferrant, O.D.</p>
  </div>

  <div class="gold-rule"></div>

  <div class="contact">
    <p class="contact__line">
      <svg class="contact__icon" viewBox="0 0 24 24" aria-hidden="true">
        <path fill="#e3b936" d="M6.6 10.8a15.1 15.1 0 0 0 6.6 6.6l2.2-2.2a1 1 0 0 1 1-.25 11.4 11.4 0 0 0 3.6.57 1 1 0 0 1 1 1V20a1 1 0 0 1-1 1A17 17 0 0 1 3 4a1 1 0 0 1 1-1h3.5a1 1 0 0 1 1 1c0 1.25.2 2.45.57 3.57a1 1 0 0 1-.25 1z"/>
      </svg>
      <span>555-014-2738</span>
    </p>
    <p class="contact__line">
      <svg class="contact__icon" viewBox="0 0 24 24" aria-hidden="true">
        <rect x="2" y="5" width="20" height="14" fill="#e3b936"/>
        <path d="M2 5l10 8 10-8" fill="none" stroke="#31383f" stroke-width="1.6"/>
      </svg>
      <span>Hello@BrightLensHub.example</span>
    </p>
    <p class="contact__line">
      <svg class="contact__icon" viewBox="0 0 24 24" aria-hidden="true">
        <g fill="none" stroke="#e3b936" stroke-width="1.8">
          <circle cx="12" cy="12" r="9.5"/>
          <ellipse cx="12" cy="12" rx="4.5" ry="9.5"/>
          <path d="M2.5 12h19M4 7h16M4 17h16"/>
        </g>
      </svg>
      <span>Www.<span class="contact__accent">BrightLensHub</span>.example</span>
    </p>
    <p class="contact__line contact__address">417 Garnet R. Holloway, Harlow Springs, ZQ 00000</p>
  </div>
</section>

<section class="card card--back">
  <div class="brand">
    <span class="brand__dot"></span>
    <span class="brand__name">brightlenshub</span>
  </div>

  <div class="appt-band">Your Next Appointment</div>

  <div class="appt-table">
    <div class="appt-table__cell appt-table__cell--date">Date</div>
    <div class="appt-table__cell appt-table__cell--time">Time</div>
  </div>

  <div class="appt-note">
    <p>If your unable to keep you appointment ,</p>
    <p>kindly give us 24 hour notice</p>
  </div>

  <div class="olive-rule"></div>
</section>

</body>
</html>
```